Kickboxing, Fitness, MMA Flyer Design Project

I would like a double sided A5 flyer please view the website www.ironwillowdojo.com.au to see what we do.
I would like all the categories listed or mentioned on the flyer that we offer under our services - http://www.ironwillowdojo.com.au/index.php/services
Please do not copy the webpage content/images I am looking for something fresh.
KTB Fitness is to be separated like I have done on the website. and to be advertised on the 2nd page.
The point I am trying to get across is we are new come and try us out and or contact us.
Please also list on the flyer- First class free.
Contact details are on the contact us page – mobile number and email web address and address is to be included.
Logos have been uploaded and i will leave required images for the designer to include.
Updates
Target Market(s)
I am targeting all people from ages 6 and up to get fit and learn kickboxing
Industry/Entity Type
Fitness
Requirements
Must have
- Iron Willow Dojo Logo on page 1
KTB Fitness Logo on page 2
An image that will portray Kickboxing, fitness, Mixed martial arts on page 1.
An image that will portray KTB Fitness, on page 2.
Should not have
- Any existing images from the website

```html
<!DOCTYPE html>
<html lang="en">
<head>
<meta charset="utf-8">
<title>Iron Willow Dojo – Flyer Front</title>
<link href="https://fonts.googleapis.com/css2?family=Oswald:wght@500;600&family=Arimo:wght@400;700&display=swap" rel="stylesheet">
<style>
  :root {
    --bg: #e9e4de;
    --paper: #ffffff;
    --ink: #0a0a0a;
    --red: #e31e24;
    --red-deep: #b8141a;
    --white: #ffffff;
  }
  * { margin: 0; padding: 0; box-sizing: border-box; }
  html, body { width: 1200px; height: 900px; overflow: hidden; background: var(--bg); }
  .canvas { position: relative; width: 1200px; height: 900px; }

  .flyer {
    position: absolute; left: 303px; top: 62px; width: 581px; height: 828px;
    background: var(--paper); overflow: hidden;
  }
  .side-band {
    position: absolute; left: 0; top: 265px; width: 100%; height: 316px; background: var(--red);
  }
  .panel {
    position: absolute; left: 17px; top: 17px; width: 548px; height: 793px;
    background: var(--ink); border-radius: 22px; overflow: hidden;
  }

  .brand {
    position: absolute; top: 14px; left: 0; width: 100%; text-align: center;
    font-family: "Oswald", sans-serif; font-weight: 600; color: var(--red);
    font-size: 31px; line-height: 34px; letter-spacing: 4px;
  }
  .trial {
    position: absolute; top: 90px; left: 0; width: 100%; text-align: center;
    font-family: "Oswald", sans-serif; font-weight: 500; color: var(--white);
    font-size: 21px; letter-spacing: 0.5px;
  }
  .free {
    position: absolute; top: 114px; left: 0; width: 100%; text-align: center;
    font-family: "Oswald", sans-serif; font-weight: 500; color: var(--red);
    font-size: 32px; letter-spacing: 0.5px;
  }

  .hero-photo {
    position: absolute; left: 0; top: 160px; width: 100%; height: 272px;
    background: radial-gradient(ellipse at 50% 55%, #4a3a33 0%, #1e1a19 45%, #080808 80%),
                linear-gradient(#111, #050505);
  }

  .promo {
    position: absolute; left: -8px; top: 431px; width: 564px; height: 74px;
    background: linear-gradient(var(--red), var(--red-deep));
    text-align: center; color: var(--white);
    font-family: "Arimo", sans-serif; font-weight: 700; text-transform: uppercase;
    padding-top: 4px;
  }
  .promo .lead { font-size: 15.5px; line-height: 17px; }
  .promo .sub { font-size: 13.5px; line-height: 15px; }
  .promo .cta { font-size: 10.5px; line-height: 15px; }

  .intro {
    position: absolute; left: 16px; top: 512px; width: 508px;
    font-family: "Arimo", sans-serif; color: var(--white);
    font-size: 14.2px; line-height: 15.6px;
  }

  .offer-list { position: absolute; top: 598px; font-family: "Arimo", sans-serif; }
  .offer-list.classes { left: 16px; }
  .offer-list.extras { left: 283px; }
  .offer-list h2 {
    color: var(--red); font-size: 13.5px; font-weight: 700; margin-bottom: 3px;
  }
  .offer-list ul { list-style: none; }
  .offer-list li {
    position: relative; padding-left: 15px; color: var(--white);
    font-size: 10.8px; font-weight: 700; line-height: 15.3px; text-transform: uppercase;
  }
  .offer-list li::before {
    content: ""; position: absolute; left: 0; top: 4px; width: 7px; height: 7px; background: var(--red);
  }

  .contact-tab {
    position: absolute; left: 129px; top: 731px; width: 325px; height: 97px;
    background: var(--white); border-radius: 40px 40px 0 0;
    text-align: center; font-family: "Arimo", sans-serif; font-style: normal; color: var(--red);
  }
  .contact-tab .phone { font-size: 26px; font-weight: 700; line-height: 30px; padding-top: 3px; }
  .contact-tab .line { font-size: 15px; line-height: 17px; }
  .contact-tab .line b { font-weight: 700; }
</style>
</head>
<body>
<div class="canvas">
  <article class="flyer">
    <div class="side-band"></div>
    <div class="panel">
      <h1 class="brand">IRON WILLOW<br>DOJO</h1>
      <p class="trial">TRIAL IRON WILLOW DOJO TODAY.</p>
      <p class="free">FIRST CLASS IS FREE.</p>

      <div class="hero-photo" role="img" aria-label="Two kickboxers sparring inside a caged ring, one throwing a high kick"></div>

      <div class="promo">
        <p class="lead">Want to get fit, lose weight, brush up on an old skill set,</p>
        <p class="sub">challenge yourself or learn some new self-defence techniques,</p>
        <p class="sub">Iron Willow Dojo can help you reach your goals!</p>
        <p class="cta">Contact us today or visit www.ironwillowdojo.com.au</p>
      </div>

      <p class="intro">Iron Willow Dojo is a new fitness and fight training facility created to cater for all ages. We welcome all levels of experience, from beginner to advanced. Our classes are designed to accomodate a range of skill levles, and our relaxed friendly atmosphere will make you feel right at home. We believe in a relaxed, supportive training environment; no egos and no attitude.</p>

      <section class="offer-list classes">
        <h2>IRON WILLOW DOJO CLASSES</h2>
        <ul>
          <li>Thai Kickboxing-MMA</li>
          <li>Street Self Defence</li>
          <li>Fitness and KTB Fitness</li>
          <li>Female Only Classes</li>
          <li>Over 35's Classes</li>
          <li>Kids Martial Arts</li>
        </ul>
      </section>

      <section class="offer-list extras">
        <h2>WE ALSO OFFER</h2>
        <ul>
          <li>Group Fitness Session</li>
          <li>Battle Rope Workouts</li>
          <li>Tyre Flipping</li>
          <li>Heavy Bag Workouts</li>
          <li>Sledgehammer Workouts</li>
          <li>Stretching and Flexibility Sessions.</li>
        </ul>
      </section>
    </div>

    <address class="contact-tab">
      <p class="phone">0400 555 019</p>
      <p class="line">info@ironwillowdojo.com.au</p>
      <p class="line">1/8 Foundry Street Lakeview QLD 4000</p>
      <p class="line">www.<b>ironwillowdojo</b>.com.au</p>
    </address>
  </article>
</div>
</body>
</html>
```